Business Card Design Project

Use our current logo. Clean design.

Industry/Entity Type

Business

Requirements
Must have
• Marisela DUBRANCQ
M. Law
Managing Partner

Alpenvorsa AG
Kornhalmweg 214
CH-3097 Liebefeld

M. +41 79 412 56 27
T. +41 31 928 44 10
F. +41 31 928 44 19

m.dubrancq@alpenvorsa-example.com
www.alpenvorsa-example.com

```html
<!DOCTYPE html>
<html lang="en">
<head>
<meta charset="utf-8">
<title>Alpenvorsa AG – Business Card</title>
<link rel="stylesheet" href="https://fonts.googleapis.com/css2?family=Source+Sans+3:wght@300;400&display=swap">
<style>
  :root {
    --backdrop: #e4e3e1;
    --card: #f1f1f0;
    --ink: #2b2b2b;
    --ink-soft: #4a4a4a;
    --accent: #c8161d;
    --shadow: rgba(0,0,0,0.14);
  }
  * { margin: 0; padding: 0; box-sizing: border-box; }
  html, body {
    width: 1200px; height: 900px; overflow: hidden;
    background: var(--backdrop);
    font-family: "Source Sans 3", "Myriad Pro", Arial, sans-serif;
    color: var(--ink);
  }
  .stage {
    width: 1200px; height: 900px;
    display: flex; align-items: center; justify-content: center; gap: 60px;
  }
  .card {
    position: relative;
    width: 520px; height: 336px;
    background: var(--card);
    box-shadow: 0 2px 3px var(--shadow), 0 12px 30px var(--shadow);
  }

  /* Front */
  .front-mark {
    position: absolute; left: 50%; top: 118px; transform: translateX(-50%);
    display: flex; align-items: center; gap: 14px;
  }
  .front-mark__square { width: 34px; height: 34px; background: var(--accent); }
  .front-mark__name {
    font-size: 34px; font-weight: 400; letter-spacing: 1px; color: var(--ink);
  }
  .front-url {
    position: absolute; left: 0; right: 0; bottom: 62px;
    text-align: center; font-size: 13px; font-weight: 400;
    letter-spacing: 3px; color: var(--ink);
  }

  /* Back */
  .contact {
    position: absolute; left: 258px; top: 34px;
    font-weight: 300; color: var(--ink-soft);
  }
  .contact__name { font-size: 21px; font-weight: 400; color: var(--ink); letter-spacing: 0.3px; }
  .contact__role { font-size: 11.5px; margin-top: 2px; }
  .contact__rule { width: 232px; height: 1px; background: var(--accent); margin: 9px 0 8px; }
  .contact__email { font-size: 12px; }
  .contact__phones { margin-top: 26px; font-size: 12.5px; line-height: 1.35; }
  .contact__phones span { display: inline-block; width: 20px; }
  .contact__address { margin-top: 18px; font-size: 12.5px; line-height: 1.35; }

  .back-mark {
    position: absolute; left: 38px; bottom: 44px;
    font-size: 30px; font-weight: 400; letter-spacing: 1px; color: var(--ink);
  }
</style>
</head>
<body>
  <main class="stage">
    <section class="card card--front" aria-label="Card front">
      <div class="front-mark">
        <div class="front-mark__square"></div>
        <div class="front-mark__name">Alpenvorsa</div>
      </div>
      <p class="front-url">www.alpenvorsa-example.com</p>
    </section>

    <section class="card card--back" aria-label="Card back">
      <div class="contact">
        <p class="contact__name">Marisela DUBRANCQ</p>
        <p class="contact__role">M. Law &nbsp;|&nbsp; Managing Partner</p>
        <div class="contact__rule"></div>
        <p class="contact__email">m.dubrancq@alpenvorsa-example.com</p>
        <p class="contact__phones">
          <span>T</span>+41 31 928 44 10<br>
          <span>M</span>+41 79 412 56 27<br>
          <span>F</span>+41 31 928 44 19
        </p>
        <p class="contact__address">
          ALPENVORSA AG<br>
          Kornhalmweg 214<br>
          CH-3097 Liebefeld
        </p>
      </div>
      <div class="back-mark">Alpenvorsa</div>
    </section>
  </main>
</body>
</html>
```